ad for food show brochure

Need to clean up this concept sketch. We are selling food at a festival but the concept isn't quite named. We're looking to create a buzz and have people sign up to be kept apprised of the progress of the chain ... or the first store. The website at the bottom is just for filler, we can add that before ad goes to print. We're not married to this text so if you come up with something better, great. also may want to have a blank @ line for twitter feed and another line for FB page.
The concept is for a Vegan Fast Food place but I need to focus more on the middle of the road diners, we'll get the vegans to come and staunch carnivores won't ever come so it's the middle of the road folks we're after. The slant and speed lines were my attempt to show speed.
Thanks.
This ad is a 5/5 x 2.125 space in the festival brochure. Need this asap.
I also think this needs to be b&w so lets go with that. Just found out COLOR is ok.
That last word in the sketch is not whose but WHERE?
The last word is WHERE not whose. Thanks
We either need to add the word Vegan in the top of the ad or add it in the sentence about all that is vegan and good in the worl.
The ad can be in color. Just to clarify, the word Vegan should be o e of the questions on top. Eithe as part of another question ... 'Vegan fast food?' Or as its own line or bubble.
- pdf file so I can change the website address.

```html
<!DOCTYPE html>
<html lang="en">
<head>
<meta charset="utf-8">
<title>Vegan Fast Food – Festival Ad</title>
<link rel="stylesheet" href="https://fonts.googleapis.com/css2?family=Nunito:wght@900&family=Open+Sans:ital,wght@0,700;0,800;1,800&family=Questrial&display=swap">
<style>
  :root {
    --green: #13996b;
    --white: #ffffff;
    --ink: #0a0a0a;
  }
  * { margin: 0; padding: 0; box-sizing: border-box; }
  html, body {
    width: 1200px;
    height: 3103px;
    overflow: hidden;
    background: var(--white);
  }
  .ad {
    position: relative;
    width: 1200px;
    height: 3103px;
    background: var(--white);
    font-family: "Open Sans", Arial, sans-serif;
  }
  .headline-vegan {
    position: absolute;
    left: 36px;
    top: 30px;
    font-family: "Nunito", "Arial Rounded MT Bold", sans-serif;
    font-weight: 900;
    font-size: 222px;
    line-height: 1;
    letter-spacing: 2px;
    color: var(--green);
  }
  .headline-band {
    position: absolute;
    left: 234px;
    top: 244px;
    width: 966px;
    height: 296px;
    background: var(--green);
    display: flex;
    align-items: center;
    justify-content: center;
  }
  .headline-band span {
    font-family: "Questrial", "Century Gothic", sans-serif;
    font-size: 206px;
    line-height: 1;
    color: var(--white);
    margin-top: 20px;
  }
  .bubble {
    position: absolute;
    top: 645px;
    height: 758px;
    background: var(--green);
    color: var(--white);
  }
  .bubble-fast {
    left: 0;
    width: 683px;
    border-radius: 0 170px 170px 0;
  }
  .bubble-nyc {
    left: 752px;
    width: 448px;
    border-radius: 330px 0 0 330px / 379px 0 0 379px;
  }
  .bubble .question {
    position: absolute;
    top: 328px;
    font-weight: 800;
    font-size: 98px;
    line-height: 1;
    white-space: nowrap;
  }
  .bubble .answer {
    position: absolute;
    top: 440px;
    font-weight: 800;
    font-style: italic;
    font-size: 82px;
    line-height: 1;
    letter-spacing: 3px;
  }
  .bubble-fast .question { left: 16px; }
  .bubble-fast .answer { right: 54px; }
  .bubble-nyc .question { left: 48px; }
  .bubble-nyc .answer { left: 172px; }
  .where-panel {
    position: absolute;
    left: 0;
    top: 1483px;
    width: 1200px;
    height: 758px;
    background: var(--green);
    color: var(--white);
    text-align: center;
  }
  .where-panel .lead {
    position: absolute;
    left: 0;
    right: 0;
    top: 80px;
    font-weight: 700;
    font-size: 70px;
    line-height: 108px;
  }
  .where-panel .where {
    position: absolute;
    left: 0;
    right: 0;
    top: 380px;
    font-weight: 800;
    font-size: 236px;
    line-height: 1;
    letter-spacing: 6px;
  }
  .website {
    position: absolute;
    left: 0;
    right: 0;
    top: 2335px;
    text-align: center;
    font-weight: 700;
    font-size: 78px;
    line-height: 1;
    color: var(--ink);
  }
  .teaser {
    position: absolute;
    left: 0;
    right: 0;
    top: 2520px;
    text-align: center;
    font-weight: 800;
    font-size: 76px;
    line-height: 112px;
    color: var(--green);
  }
</style>
</head>
<body>
  <main class="ad">
    <div class="headline-vegan">VEGAN</div>
    <div class="headline-band"><span>Fast Food</span></div>

    <div class="bubble bubble-fast">
      <div class="question">FAST FOOD?</div>
      <div class="answer">YEP..</div>
    </div>
    <div class="bubble bubble-nyc">
      <div class="question">IN NYC?</div>
      <div class="answer">YEP..</div>
    </div>

    <section class="where-panel">
      <p class="lead">In the name of all that<br>is good in the world</p>
      <p class="where">WHERE ?</p>
    </section>

    <p class="website">www.greenlane-eats.com</p>

    <p class="teaser">Until Then, You Can<br>Enjoy Our<br>Vegan Drumsticks</p>
  </main>
</body>
</html>
```